Sportswear for local soccer teams Ad

Looking for a banner ad to be placed in a local soccer associations website. Brawlinmoor Logo must be shown. It should be short, eyecatching and want teams to visit or contact us about their kits or training apparel. Brawlinmoor is a doric word for delighted so any play on happiness, delight is fine. Size allowable is : 605x80. Also looking for a Skyscraper to be placed on all subsequent pages on their site. Size : 240x900

Target Market(s)

Football Teams

Industry/Entity Type

Sports Bar

```html
<!DOCTYPE html>
<html lang="en">
<head>
<meta charset="utf-8">
<title>Brawlinmoor Banner Ads</title>
<link rel="stylesheet" href="https://fonts.googleapis.com/css2?family=Barlow+Condensed:ital,wght@0,600;1,500;1,700;1,800&display=swap">
<style>
  :root {
    --page: #f2f2f2;
    --navy: #0d3f7a;
    --blue-dark: #0b3a72;
    --blue-mid: #1d5ea6;
    --orange: #f39a1d;
    --orange-deep: #e0740b;
    --yellow: #ffc20e;
    --white: #ffffff;
    --red: #e5121b;
    --red-dark: #a8070d;
    --grass-light: #7cbf3a;
    --grass-dark: #3f8a24;
  }
  * { margin: 0; padding: 0; box-sizing: border-box; }
  html, body { width: 1200px; height: 1200px; overflow: hidden; background: var(--page); }
  body { position: relative; font-family: "Barlow Condensed", sans-serif; }

  .ad { position: absolute; overflow: hidden; border: 1px solid var(--navy); background: var(--white); }
  .ad-bg { position: absolute; inset: 0; width: 100%; height: 100%; }
  .ad > * { position: absolute; }

  .brand { display: flex; flex-direction: column; align-items: center; }
  .brand-dot { border-radius: 50%; background: var(--orange); }
  .brand-name { font-weight: 600; color: var(--navy); letter-spacing: 0.5px; line-height: 1; margin-top: 6px; }

  .headline { text-align: center; font-style: italic; text-transform: uppercase; line-height: 1; color: var(--white); font-weight: 500; }
  .headline .accent { color: var(--yellow); font-weight: 800; }

  .shop-btn { display: flex; border-radius: 4px; overflow: hidden; box-shadow: 0 2px 3px rgba(0,0,0,0.35); }
  .shop-label { flex: 1; background: var(--red); color: var(--white); font-style: italic; font-weight: 800; display: flex; align-items: center; justify-content: center; }
  .shop-cart { background: var(--red-dark); display: flex; align-items: center; justify-content: center; }

  /* Leaderboard */
  .leaderboard { left: 78px; top: 77px; width: 1043px; height: 137px; }
  .leaderboard .brand { left: 10px; top: 14px; width: 190px; }
  .leaderboard .brand-dot { width: 60px; height: 60px; }
  .leaderboard .brand-name { font-size: 28px; }
  .leaderboard .headline { left: 240px; top: 20px; width: 420px; font-size: 46px; }
  .leaderboard .headline .accent { font-size: 50px; }
  .leaderboard .shop-btn { left: 660px; top: 48px; width: 183px; height: 44px; }
  .leaderboard .shop-label { font-size: 27px; }
  .leaderboard .shop-cart { width: 56px; }

  /* Skyscraper */
  .skyscraper { left: 484px; top: 244px; width: 234px; height: 879px; }
  .skyscraper .brand { left: 0; top: 18px; width: 234px; }
  .skyscraper .brand-dot { width: 72px; height: 72px; }
  .skyscraper .brand-name { font-size: 32px; }
  .skyscraper .headline { left: 0; top: 228px; width: 234px; font-size: 52px; line-height: 0.98; }
  .skyscraper .headline .accent { font-size: 62px; display: block; line-height: 1.02; }
  .skyscraper .shop-btn { left: 18px; top: 553px; width: 200px; height: 48px; }
  .skyscraper .shop-label { font-size: 30px; }
  .skyscraper .shop-cart { width: 60px; }
</style>
</head>
<body>

<section class="ad leaderboard" aria-label="Brawlinmoor leaderboard ad">
  <svg class="ad-bg" viewBox="0 0 1043 137" preserveAspectRatio="none">
    <defs>
      <linearGradient id="lb-blue" x1="0" y1="0" x2="0" y2="1">
        <stop offset="0" stop-color="#1d5ea6"/><stop offset="0.5" stop-color="#175299"/><stop offset="1" stop-color="#0b3a72"/>
      </linearGradient>
      <linearGradient id="lb-grass" x1="0" y1="0" x2="0" y2="1">
        <stop offset="0" stop-color="#8bc34a"/><stop offset="0.5" stop-color="#5ea332"/><stop offset="1" stop-color="#3f8a24"/>
      </linearGradient>
    </defs>
    <rect width="1043" height="137" fill="url(#lb-blue)"/>
    <polygon points="0,0 252,0 207,137 0,137" fill="#ffffff"/>
    <polygon points="252,0 270,0 225,137 207,137" fill="#f39a1d"/>
    <polygon points="808,0 826,0 764,137 746,137" fill="#f39a1d"/>
    <polygon role="img" aria-label="Photo of soccer players' legs and a ball on a grass pitch" points="826,0 1043,0 1043,137 764,137" fill="url(#lb-grass)"/>
  </svg>
  <div class="brand">
    <span class="brand-dot"></span>
    <span class="brand-name">BRAWLINMOOR</span>
  </div>
  <h2 class="headline">Experience the<br><span class="accent">‘Brawlinmoor’</span> feeling</h2>
  <a class="shop-btn">
    <span class="shop-label">SHOP NOW</span>
    <span class="shop-cart">
      <svg width="30" height="26" viewBox="0 0 30 26" fill="none" stroke="#fff" stroke-width="2.4" stroke-linejoin="round"><path d="M1 2h5l4 15h15l3-11H8"/><path d="M11 9h15M12 13h12"/><circle cx="12" cy="22" r="2" fill="#fff"/><circle cx="23" cy="22" r="2" fill="#fff"/></svg>
    </span>
  </a>
</section>

<section class="ad skyscraper" aria-label="Brawlinmoor skyscraper ad">
  <svg class="ad-bg" viewBox="0 0 234 879" preserveAspectRatio="none">
    <defs>
      <linearGradient id="sk-blue" x1="0" y1="0" x2="1" y2="0">
        <stop offset="0" stop-color="#0b3a72"/><stop offset="0.5" stop-color="#1d5ea6"/><stop offset="1" stop-color="#0b3a72"/>
      </linearGradient>
      <linearGradient id="sk-grass" x1="0" y1="0" x2="0" y2="1">
        <stop offset="0" stop-color="#6fb13c"/><stop offset="0.6" stop-color="#5ea332"/><stop offset="1" stop-color="#3f8a24"/>
      </linearGradient>
    </defs>
    <rect width="234" height="879" fill="url(#sk-blue)"/>
    <polygon points="0,0 234,0 234,151 0,201" fill="#ffffff"/>
    <polygon points="0,201 234,151 234,160 0,212" fill="#f39a1d"/>
    <polygon points="0,622 234,562 234,572 0,632" fill="#f39a1d"/>
    <polygon role="img" aria-label="Photo of a soccer player dribbling a ball on a grass pitch" points="0,632 234,572 234,879 0,879" fill="url(#sk-grass)"/>
  </svg>
  <div class="brand">
    <span class="brand-dot"></span>
    <span class="brand-name">BRAWLINMOOR</span>
  </div>
  <h2 class="headline">Experience<br>the<span class="accent">‘Brawl-<br>inmoor’</span>feeling</h2>
  <a class="shop-btn">
    <span class="shop-label">SHOP NOW</span>
    <span class="shop-cart">
      <svg width="32" height="28" viewBox="0 0 30 26" fill="none" stroke="#fff" stroke-width="2.4" stroke-linejoin="round"><path d="M1 2h5l4 15h15l3-11H8"/><path d="M11 9h15M12 13h12"/><circle cx="12" cy="22" r="2" fill="#fff"/><circle cx="23" cy="22" r="2" fill="#fff"/></svg>
    </span>
  </a>
</section>

</body>
</html>
```